Profesional personal website needs design and business card

I need a business card with my professional name as a logo "Marlo Vitality" for my business. I am a Wellness Coach, consultant and trainer. So it should be professional, wellness oriented and modern.

Target Market(s)

Private clients, governments, corporations. Luxury and high market.

Industry/Entity Type

Health And Wellness

Contact Information for Business Card

Marlo Vitality should be the logo

Colors

Designer to choose colors to be used in the design.

Requirements
Must have
• Marlo Vitality
• Name: Tomás Arribal
• Wellness Coach, Consultant & Trainer.
• Website: www.marlovitality.example
• Phone:
• Spain (+34) 612 480 397
• (USA) +1 (555) 318 2046
Nice to have
• The most important is the design of "Marlo Vitality", as this is going to be my personal brand logo. It should be professional, wellness, high end and actual.
Should not have
• no golds, no baroque style..

```html
<!DOCTYPE html>
<html lang="en">
<head>
<meta charset="utf-8">
<title>Marlo Vitality — Business Card</title>
<link rel="stylesheet" href="https://fonts.googleapis.com/css2?family=Cinzel:wght@700&family=Lato:wght@300;400;700&family=Raleway:wght@300&display=swap">
<style>
  :root {
    --navy: #0a243b;
    --sage: #94b8a3;
    --white: #ffffff;
    --page: #ffffff;
  }
  * { box-sizing: border-box; margin: 0; padding: 0; }
  html, body {
    width: 1120px;
    height: 1200px;
    overflow: hidden;
    background: var(--page);
  }
  .canvas {
    position: relative;
    width: 1120px;
    height: 1200px;
  }
  .card {
    position: absolute;
    left: 144px;
    width: 828px;
    height: 473px;
    background: var(--navy);
    overflow: hidden;
  }
  .card--front { top: 0; }
  .card--back { top: 647px; }

  /* Front */
  .brand-mark {
    position: absolute;
    left: 50%;
    top: 124px;
    transform: translateX(-50%);
  }
  .brand-name {
    position: absolute;
    left: 0;
    right: 0;
    top: 256px;
    text-align: center;
    color: var(--sage);
    font-weight: normal;
  }
  .brand-name__main {
    display: block;
    font-family: "Cinzel", serif;
    font-weight: 700;
    font-size: 80px;
    letter-spacing: 8px;
    line-height: 1;
    padding-left: 8px;
  }
  .brand-name__sub {
    display: block;
    margin-top: 8px;
    font-family: "Raleway", sans-serif;
    font-weight: 300;
    font-size: 31px;
    letter-spacing: 13px;
    line-height: 1;
    padding-left: 13px;
  }

  /* Back */
  .corner-mark {
    position: absolute;
    right: 17px;
    top: 22px;
  }
  .identity {
    position: absolute;
    left: 0;
    right: 0;
    top: 138px;
    text-align: center;
    font-family: "Lato", sans-serif;
  }
  .identity__name {
    font-size: 58px;
    line-height: 1;
    letter-spacing: 6px;
    padding-left: 6px;
    color: var(--sage);
    white-space: nowrap;
  }
  .identity__first { font-weight: 700; }
  .identity__last { font-weight: 300; }
  .identity__role {
    margin-top: 4px;
    font-size: 20px;
    line-height: 1;
    font-weight: 400;
    letter-spacing: 3.6px;
    padding-left: 3.6px;
    color: var(--white);
    white-space: nowrap;
  }
  .contact-band {
    position: absolute;
    left: 0;
    right: 0;
    top: 346px;
    height: 52px;
    background: var(--white);
    font-family: "Lato", sans-serif;
    font-weight: 300;
    font-size: 27px;
    color: var(--navy);
  }
  .contact-band__phone {
    position: absolute;
    top: 50%;
    transform: translate(-50%, -50%);
    white-space: nowrap;
    line-height: 1;
  }
  .contact-band__phone--spain { left: 206px; }
  .contact-band__phone--usa { left: 619px; }
  .contact-band__divider {
    position: absolute;
    left: 412px;
    top: 14px;
    width: 3px;
    height: 25px;
    background: var(--navy);
  }
  .website {
    position: absolute;
    left: 0;
    right: 0;
    top: 418px;
    text-align: center;
    font-family: "Lato", sans-serif;
    font-weight: 400;
    font-size: 26px;
    line-height: 1;
    letter-spacing: 3.3px;
    color: var(--sage);
  }
</style>
</head>
<body>
<main class="canvas">
  <section class="card card--front" aria-label="Card front">
    <svg class="brand-mark" width="96" height="96" viewBox="0 0 96 96" aria-hidden="true">
      <circle cx="48" cy="48" r="45" fill="none" stroke="var(--sage)" stroke-width="2.5"/>
    </svg>
    <h1 class="brand-name">
      <span class="brand-name__main">MARLO</span>
      <span class="brand-name__sub">VITALITY</span>
    </h1>
  </section>

  <section class="card card--back" aria-label="Card back">
    <svg class="corner-mark" width="54" height="54" viewBox="0 0 54 54" aria-hidden="true">
      <circle cx="27" cy="27" r="25" fill="none" stroke="var(--sage)" stroke-width="2"/>
    </svg>
    <div class="identity">
      <h2 class="identity__name"><span class="identity__first">TOMÁS</span> <span class="identity__last">ARRIBAL</span></h2>
      <p class="identity__role">WELLNESS COACH - CONSULTANT - TRAINER</p>
    </div>
    <div class="contact-band">
      <span class="contact-band__phone contact-band__phone--spain">Spain (+34) 612 480 397</span>
      <span class="contact-band__divider"></span>
      <span class="contact-band__phone contact-band__phone--usa">USA +1 (555) 318 2046</span>
    </div>
    <p class="website">www.marlovitality.example</p>
  </section>
</main>
</body>
</html>
```